Ambulance Full Vehicle Wrap - Local Roof Cleaning Business

I need a full vehicle wrap design for a 2003 Z620 ambulance. Attached are photos with dimensions and the logo file. Also, I've attached a rough mock-up of one concept, but I'm open to new ideas. I need the design to include:

Phone: 866-5-TIDYTOP
Website: tidytophouse.com
"Always Clean Guarantee"
"Safe for Roofs, Pets, and Plants"

Font styles to use
Sans Serif

```html
<!DOCTYPE html>
<html lang="en">
<head>
<meta charset="utf-8">
<title>TidyTop House – Vehicle Wrap Panels</title>
<link href="https://fonts.googleapis.com/css2?family=Oswald:wght@500;600&family=Open+Sans:wght@700&display=swap" rel="stylesheet">
<style>
  :root{
    --paper:#ffffff;
    --ink:#111111;
    --navy:#15386e;
    --deep:#1a4f8f;
    --mid:#1f73b7;
    --sky:#3fb6e6;
    --ice:#d9f3fb;
    --red:#e3202e;
    --line-blue:#35b7ee;
    --badge:#2a2a2a;
  }
  html,body{margin:0;padding:0;width:1200px;height:2503px;overflow:hidden;background:var(--paper);}
  .sheet{position:relative;width:1200px;height:2503px;}
  .panel{position:absolute;display:block;}
  .panel--side{left:60px;top:688px;width:1080px;height:485px;}
  .panel--back{left:296px;top:1308px;width:607px;height:485px;}
  .panel--door{left:331px;top:1944px;width:537px;height:409px;}
  .spec{position:absolute;left:0;width:1200px;text-align:center;margin:0;
        font:700 32px/1 "Open Sans",sans-serif;color:var(--ink);}
  .spec--side{top:1196px;}
  .spec--back{top:1836px;}
  .spec--door{top:2400px;}
  .wrap-text{font-family:"Oswald",sans-serif;}
  .brand-name{font-family:"Oswald",sans-serif;font-weight:600;fill:#ffffff;}
</style>
</head>
<body>
<main class="sheet">

  <!-- Side panel -->
  <svg class="panel panel--side" viewBox="0 0 1080 485" aria-label="Side wrap panel">
    <defs>
      <linearGradient id="sideBg" x1="0" y1="0" x2="0" y2="1">
        <stop offset="0" stop-color="#4fc4ea"/>
        <stop offset=".55" stop-color="#1f86c6"/>
        <stop offset="1" stop-color="#1a4f8f"/>
      </linearGradient>
      <radialGradient id="sideBurst" cx=".72" cy=".35" r=".45">
        <stop offset="0" stop-color="#e9fbff"/>
        <stop offset=".5" stop-color="#52c6ec" stop-opacity=".7"/>
        <stop offset="1" stop-color="#1f86c6" stop-opacity="0"/>
      </radialGradient>
      <linearGradient id="sidePhoto" x1="0" y1="0" x2="0" y2="1">
        <stop offset="0" stop-color="#a9cde6"/>
        <stop offset=".5" stop-color="#dbe8f1"/>
        <stop offset="1" stop-color="#5d6c7c"/>
      </linearGradient>
      <linearGradient id="lowBlue" x1="0" y1="0" x2="1" y2="0">
        <stop offset="0" stop-color="#5aa9dc"/>
        <stop offset="1" stop-color="#16427d"/>
      </linearGradient>
      <linearGradient id="pill" x1="0" y1="0" x2="0" y2="1">
        <stop offset="0" stop-color="#1d4f92"/>
        <stop offset="1" stop-color="#102f5f"/>
      </linearGradient>
      <linearGradient id="badge" x1="0" y1="0" x2="0" y2="1">
        <stop offset="0" stop-color="#555"/>
        <stop offset="1" stop-color="#1c1c1c"/>
      </linearGradient>
    </defs>
    <rect width="1080" height="485" fill="url(#sideBg)"/>
    <rect width="1080" height="485" fill="url(#sideBurst)"/>
    <g role="img" aria-label="Photo: worker pressure-washing a tiled roof under a cloudy sky">
      <path d="M0 0H560V330Q300 345 0 365Z" fill="url(#sidePhoto)"/>
    </g>
    <path d="M0 485V372Q540 340 1080 225V485Z" fill="url(#lowBlue)"/>
    <path d="M0 352Q540 320 1080 200V222Q540 340 0 372Z" fill="var(--red)"/>
    <path d="M0 372Q540 340 1080 222V232Q540 350 0 380Z" fill="var(--line-blue)"/>
    <text class="brand-name" x="830" y="205" font-size="104" text-anchor="middle">TIDYTOP</text>
    <text class="brand-name" x="830" y="315" font-size="104" text-anchor="middle">HOUSE</text>
    <rect x="70" y="362" width="370" height="60" rx="14" fill="url(#pill)" stroke="#cfe3f3" stroke-width="4"/>
    <text class="wrap-text" x="255" y="404" font-size="33" font-weight="500" fill="#fff" text-anchor="middle">Always Clean Guarantee</text>
    <rect x="40" y="442" width="116" height="36" rx="6" fill="url(#badge)" stroke="#ccc" stroke-width="2"/>
    <text class="wrap-text" x="98" y="471" font-size="27" font-weight="600" fill="#fff" text-anchor="middle" letter-spacing="1">SAFE FOR</text>
    <text class="wrap-text" x="167" y="471" font-size="27" font-weight="600" fill="#fff" letter-spacing="1">ROOFS, PETS, AND PLANTS</text>
  </svg>
  <p class="spec spec--side">SIDE&nbsp; 169” X 76”</p>

  <!-- Back panel -->
  <svg class="panel panel--back" viewBox="0 0 607 485" aria-label="Back wrap panel">
    <defs>
      <radialGradient id="backBurst" cx=".5" cy=".3" r=".75">
        <stop offset="0" stop-color="#ffffff"/>
        <stop offset=".35" stop-color="#8fdcf3"/>
        <stop offset=".75" stop-color="#1fa2d8"/>
        <stop offset="1" stop-color="#1a77b9"/>
      </radialGradient>
      <linearGradient id="backLow" x1="0" y1="0" x2="1" y2="0">
        <stop offset="0" stop-color="#5aa9dc"/>
        <stop offset="1" stop-color="#174883"/>
      </linearGradient>
    </defs>
    <rect width="607" height="485" fill="url(#backBurst)"/>
    <path d="M0 485V378Q300 350 607 310V485Z" fill="url(#backLow)"/>
    <path d="M0 358Q300 335 607 290V310Q300 355 0 378Z" fill="var(--red)"/>
    <path d="M0 378Q300 355 607 310V318Q300 363 0 385Z" fill="var(--line-blue)"/>
    <text class="brand-name" x="304" y="118" font-size="62" text-anchor="middle">TIDYTOP</text>
    <text class="brand-name" x="304" y="180" font-size="62" text-anchor="middle">HOUSE</text>
    <circle cx="58" cy="262" r="18" fill="var(--navy)"/>
    <path d="M51 253c2-2 4-2 5 0l2 4c1 2 0 3-1 4 1 3 3 5 6 6 1-1 2-2 4-1l4 2c2 1 2 3 0 5-3 3-8 2-13-3s-6-10-3-13z" fill="#fff" transform="translate(-2 -2)"/>
    <text class="wrap-text" x="86" y="273" font-size="28" font-weight="500" fill="var(--red)">866-5-TIDYTOP</text>
    <g fill="none" stroke="var(--navy)" stroke-width="2.5">
      <circle cx="366" cy="262" r="17"/>
      <ellipse cx="366" cy="262" rx="7" ry="17"/>
      <path d="M349 262h34M352 253h28M352 271h28"/>
    </g>
    <text class="wrap-text" x="392" y="273" font-size="28" font-weight="500" fill="var(--red)" textLength="186" lengthAdjust="spacingAndGlyphs">tidytophouse.com</text>
    <rect x="128" y="332" width="374" height="60" rx="14" fill="url(#pill)" stroke="#cfe3f3" stroke-width="4"/>
    <text class="wrap-text" x="315" y="374" font-size="33" font-weight="500" fill="#fff" text-anchor="middle">Always Clean Guarantee</text>
    <rect x="96" y="414" width="116" height="36" rx="6" fill="url(#badge)" stroke="#ccc" stroke-width="2"/>
    <text class="wrap-text" x="154" y="443" font-size="27" font-weight="600" fill="#fff" text-anchor="middle" letter-spacing="1">SAFE FOR</text>
    <text class="wrap-text" x="223" y="443" font-size="27" font-weight="600" fill="#fff" letter-spacing="1">ROOFS, PETS, AND PLANTS</text>
  </svg>
  <p class="spec spec--back">BACK&nbsp; 95” X 76”</p>

  <!-- Door panel -->
  <svg class="panel panel--door" viewBox="0 0 537 409" aria-label="Door wrap panel">
    <defs>
      <radialGradient id="doorBg" cx=".5" cy=".4" r=".7">
        <stop offset="0" stop-color="#27a3dc"/>
        <stop offset=".7" stop-color="#1d6fb4"/>
        <stop offset="1" stop-color="#1a4f8f"/>
      </radialGradient>
      <linearGradient id="doorLow" x1="0" y1="0" x2="1" y2="0">
        <stop offset="0" stop-color="#1c3f78"/>
        <stop offset="1" stop-color="#1d6fa8"/>
      </linearGradient>
    </defs>
    <rect width="537" height="409" fill="url(#doorBg)"/>
    <path d="M0 409V298Q250 378 537 382V409Z" fill="url(#doorLow)"/>
    <path d="M0 248Q250 350 537 362V378Q250 370 0 290Z" fill="var(--red)"/>
    <path d="M0 290Q250 370 537 378V384Q250 377 0 298Z" fill="var(--line-blue)"/>
    <circle cx="300" cy="250" r="16" fill="var(--navy)"/>
    <path d="M293 241c2-2 4-2 5 0l2 4c1 2 0 3-1 4 1 3 3 5 6 6 1-1 2-2 4-1l4 2c2 1 2 3 0 5-3 3-8 2-13-3s-6-10-3-13z" fill="#fff" transform="translate(-1 -1)"/>
    <text class="wrap-text" x="324" y="260" font-size="26" font-weight="500" fill="var(--red)">866-5-TIDYTOP</text>
    <g fill="none" stroke="var(--navy)" stroke-width="2.5">
      <circle cx="300" cy="298" r="16"/>
      <ellipse cx="300" cy="298" rx="6.5" ry="16"/>
      <path d="M284 298h32M287 290h26M287 306h26"/>
    </g>
    <text class="wrap-text" x="322" y="307" font-size="26" font-weight="500" fill="var(--red)" textLength="170" lengthAdjust="spacingAndGlyphs">tidytophouse.com</text>
  </svg>
  <p class="spec spec--door">DOOR&nbsp; 95” X 76”</p>

</main>
</body>
</html>
```